High-end Investment firm website

It needs to feel very high-end. We like clean design which incorporates a good deal of white space with the use of imagery to be provided.

Here are a few examples of design which is appealing:
https://www.brindlecrestcapital.example
https://www.larkmoorgroup.example

Please use the following shade of blue in the design #7BAFD4.

Additional brand colors black, grey and white.

This quorvex doc has a link to all of the content for the site. It also has detailed design notes per section.

https://files.quorvexdocs.example/document/d/7TRQ2WpeLmnb8cvdKa3HJ0XsNf5ZgR1YtUoC9eV4qAs/edit?usp=sharing

Target Market(s)

Investors and companies in our target industries

Industry/Entity Type

Investment

Coding

Coded - Design and coding required

Number of Pages Required

5+ page

Font styles to use
Sans Serif

Requirements
Must have
• Clean feel, lots of white space.
Nice to have
• Clean graphics similar to https://www.brindlecrestcapital.example

```html
<!DOCTYPE html>
<html lang="en">
<head>
<meta charset="utf-8">
<title>Altavance Industries</title>
<link href="https://fonts.googleapis.com/css2?family=Lato:wght@300;400;700&family=Arimo:wght@400;700&display=swap" rel="stylesheet">
<style>
:root{
  --brand-blue:#7BAFD4;
  --accent-blue:#3a9ad9;
  --ink:#1d1d1d;
  --text:#333333;
  --grey:#9c9c9c;
  --white:#ffffff;
  --footer:#2b2f36;
}
*{margin:0;padding:0;box-sizing:border-box}
html,body{width:1200px;height:3437px;overflow:hidden}
body{position:relative;font-family:'Lato',sans-serif;color:var(--text);background:var(--white)}
.abs{position:absolute}

/* hero */
.hero{left:0;top:0;width:1200px;height:600px;overflow:hidden}
.hero-photo{position:absolute;inset:0;background:linear-gradient(120deg,#5b84b8 0%,#8fb6dc 45%,#b8cfe0 70%,#7f9fc4 100%)}
.hero-shade{position:absolute;inset:0}
.brand{position:absolute;color:var(--white);font-family:'Lato',sans-serif;font-weight:400;letter-spacing:1px;text-align:center;line-height:1.15}
.hero .brand{left:110px;top:80px;width:180px;font-size:26px}
.nav{position:absolute;top:54px;left:430px;display:flex;gap:0;font-size:15px;font-weight:700;color:var(--white)}
.nav a{color:var(--white);text-decoration:none;margin-right:32px;padding-bottom:4px}
.nav a.active{color:#1c3550;border-bottom:2px solid #1c3550}
.hero-title{position:absolute;left:85px;top:423px;font-size:40px;font-weight:400;line-height:45px;color:var(--white)}

/* about */
.about-eyebrow{left:113px;top:746px;font-size:15px;font-weight:700;color:var(--accent-blue)}
.about-title{left:112px;top:766px;font-size:48px;font-weight:300;letter-spacing:1px;color:#222}
.about-copy{left:113px;top:828px;width:540px;font-size:14.5px;line-height:27.5px;color:#333}
.btn-outline{left:113px;top:995px;width:152px;height:47px;border:1.5px solid var(--accent-blue);font-size:15px;color:#333;display:flex;align-items:center;justify-content:center}
.about-visual{left:600px;top:686px;width:488px;height:423px}

/* focus */
.focus{left:0;top:1148px;width:1200px;height:521px;background:var(--brand-blue)}
.focus h2{position:absolute;top:72px;width:1200px;text-align:center;font-size:36px;font-weight:300;letter-spacing:1px;color:var(--white)}
.focus-item{position:absolute;width:200px;text-align:center;color:var(--white);font-size:17px;font-weight:700;line-height:24px}
.focus-item svg{display:block;margin:0 auto 12px}

/* capital band */
.capital{left:0;top:1669px;width:1200px;height:544px;background:linear-gradient(180deg,#b9c4cf 0%,#d8c7bd 28%,#8ea3b6 52%,#5d6c79 75%,#3d4149 100%)}
.capital-card{left:111px;top:1696px;width:429px;height:256px;background:var(--white);padding:30px 32px;font-size:18px;line-height:31px;color:#444;text-align:justify}
.capital-card strong{font-weight:400;font-size:30px;color:var(--accent-blue)}

/* experience */
.wordmark{position:absolute;font-family:'Lato',sans-serif;font-weight:400;color:var(--grey);font-size:30px;text-align:center;white-space:nowrap}
.exp-title{left:0;top:2365px;width:1200px;text-align:center;font-size:34px;font-weight:400;color:var(--accent-blue)}
.exp-copy{left:300px;top:2418px;width:600px;text-align:center;font-family:'Arimo',sans-serif;font-size:17px;line-height:32px;color:#222}

/* team */
.team{left:0;top:2614px;width:1200px;height:483px;background:var(--brand-blue)}
.team h2{position:absolute;top:76px;width:1200px;text-align:center;font-size:34px;font-weight:400;color:var(--white)}
.member{position:absolute;top:150px;width:258px;text-align:center;color:var(--white);font-family:'Arimo',sans-serif}
.portrait{width:168px;height:168px;border-radius:50%;margin:0 auto;background:linear-gradient(160deg,#3e5f9c,#2a3d66)}
.member h3{margin-top:20px;font-size:17px;font-weight:700}
.member p{margin-top:4px;font-size:13.5px;line-height:24px;padding:0 30px}
.arrow{position:absolute;top:226px;width:36px;height:36px;border:1.5px solid var(--white);border-radius:50%}

/* footer */
.footer{left:0;top:3097px;width:1200px;height:340px;background:linear-gradient(180deg,#3a4150 0%,#2a2e36 60%,#1f2228 100%);color:var(--white)}
.footer .brand{left:110px;top:166px;width:200px;font-size:27px}
.foot-col{position:absolute;top:70px}
.foot-col h4{font-size:17px;font-weight:700;margin-bottom:12px}
.foot-col li{list-style:none;font-size:14px;line-height:28px}
.social{display:flex;gap:15px;margin-top:14px}
.social span{width:32px;height:32px;border-radius:50%;background:var(--accent-blue)}
.foot-rule{position:absolute;left:110px;top:286px;width:978px;height:1px;background:rgba(255,255,255,.45)}
.copyright{position:absolute;top:298px;width:1200px;text-align:center;font-family:'Arimo',sans-serif;font-size:16px}
</style>
</head>
<body>

<svg width="0" height="0" style="position:absolute">
  <defs>
    <symbol id="ic-shield" viewBox="0 0 70 70">
      <g fill="none" stroke="#1d1d1d" stroke-width="3" stroke-linejoin="round">
        <path d="M35 5 L60 14 V34 C60 50 48 60 35 66 C22 60 10 50 10 34 V14 Z"/>
        <circle cx="35" cy="35" r="15"/>
        <polygon points="35,25 38,32 45,32 39.5,37 41.5,44 35,40 28.5,44 30.5,37 25,32 32,32"/>
      </g>
    </symbol>
    <symbol id="ic-monitor" viewBox="0 0 70 70">
      <g fill="none" stroke="#1d1d1d" stroke-width="3" stroke-linejoin="round">
        <rect x="6" y="14" width="58" height="36" rx="2"/>
        <line x1="6" y1="44" x2="64" y2="44"/>
        <path d="M28 50 L26 60 H44 L42 50"/>
        <line x1="20" y1="62" x2="50" y2="62"/>
        <rect x="27" y="26" width="16" height="13"/>
        <path d="M30 26 V20 A5 5 0 0 1 40 20 V26"/>
      </g>
    </symbol>
    <symbol id="ic-factory" viewBox="0 0 70 70">
      <g fill="none" stroke="#1d1d1d" stroke-width="3" stroke-linejoin="round">
        <path d="M5 62 V8 H14 V62"/>
        <path d="M14 62 V30 L25 22 V30 L36 22 V30 L47 22 V30 L58 22 V30 H65 V62 Z"/>
        <rect x="22" y="40" width="34" height="8"/>
        <line x1="14" y1="54" x2="65" y2="54"/>
      </g>
    </symbol>
    <symbol id="ic-building" viewBox="0 0 70 70">
      <g fill="none" stroke="#1d1d1d" stroke-width="3" stroke-linejoin="round">
        <rect x="18" y="6" width="34" height="36"/>
        <path d="M24 14 H30 M36 14 H46 M24 22 H30 M36 22 H46 M24 30 H30 M36 30 H46"/>
        <path d="M8 44 H62 L58 54 H12 Z"/>
        <path d="M14 54 L20 64 H50 L56 54"/>
      </g>
    </symbol>
    <symbol id="ic-gear" viewBox="0 0 70 70">
      <g fill="none" stroke="#1d1d1d" stroke-width="3" stroke-linejoin="round">
        <circle cx="35" cy="33" r="22"/>
        <circle cx="35" cy="33" r="12"/>
        <circle cx="35" cy="33" r="4"/>
        <path d="M35 6 V11 M35 55 V60 M8 33 H13 M57 33 H62 M16 14 L19 17 M51 49 L54 52 M54 14 L51 17 M19 49 L16 52"/>
        <path d="M28 58 V66 H42 V58"/>
      </g>
    </symbol>
  </defs>
</svg>

<!-- Hero -->
<section class="hero abs">
  <div class="hero-photo" role="img" aria-label="Robotic arms in an automated factory, tinted blue"></div>
  <svg class="hero-shade" width="1200" height="600" aria-hidden="true">
    <polygon points="0,0 0,600 770,600 280,0" fill="#1d3f73" opacity="0.5"/>
  </svg>
  <div class="brand">Altavance<br>Industries</div>
  <nav class="nav">
    <a class="active">HOME</a><a>ABOUT US</a><a>INVESTMENT FOCUS</a><a>INDUSTRY FOCUS</a><a>CONTACT US</a>
  </nav>
  <h1 class="hero-title">Partnering with<br>Exceptional Leaders<br>Building World - Class Companies</h1>
</section>

<!-- About -->
<div class="about-eyebrow abs">WHO WE ARE</div>
<h2 class="about-title abs">ABOUT US</h2>
<p class="about-copy abs">Altavance Industries focuses on opportunities where it can support senior management to drive rapid growth and profit improvement through capital infusion, technology innovation and organizational expertise.<br>We invest across a variety of growth industries with an emphasis on reshoring and rebuilding America.</p>
<div class="btn-outline abs">READ MORE</div>
<svg class="about-visual abs" viewBox="0 0 488 423" role="img" aria-label="Night city skyline seen within a triangular frame">
  <defs>
    <linearGradient id="cityTone" x1="0" y1="0" x2="0" y2="1">
      <stop offset="0" stop-color="#3f6fc7"/>
      <stop offset="0.55" stop-color="#274f9a"/>
      <stop offset="1" stop-color="#122a55"/>
    </linearGradient>
  </defs>
  <polygon points="244,0 488,423 0,423" fill="url(#cityTone)"/>
</svg>

<!-- Areas of focus -->
<section class="focus abs">
  <h2>AREAS OF FOCUS</h2>
  <div class="focus-item" style="left:100px;top:150px"><svg width="70" height="70"><use href="#ic-shield"/></svg>Defense</div>
  <div class="focus-item" style="left:300px;top:150px"><svg width="70" height="70"><use href="#ic-monitor"/></svg>Cyber Security</div>
  <div class="focus-item" style="left:500px;top:150px"><svg width="70" height="70"><use href="#ic-factory"/></svg>Industrials</div>
  <div class="focus-item" style="left:700px;top:150px"><svg width="70" height="70"><use href="#ic-building"/></svg>Digital Enterprise</div>
  <div class="focus-item" style="left:898px;top:150px"><svg width="70" height="70"><use href="#ic-gear"/></svg>Technology and<br>Professional</div>
  <div class="focus-item" style="left:100px;top:322px"><svg width="70" height="70"><use href="#ic-shield"/></svg>Defense</div>
  <div class="focus-item" style="left:300px;top:322px"><svg width="70" height="70"><use href="#ic-monitor"/></svg>Cyber Security</div>
  <div class="focus-item" style="left:500px;top:322px"><svg width="70" height="70"><use href="#ic-factory"/></svg>Industrials</div>
  <div class="focus-item" style="left:700px;top:322px"><svg width="70" height="70"><use href="#ic-building"/></svg>Digital Enterprise</div>
  <div class="focus-item" style="left:898px;top:322px"><svg width="70" height="70"><use href="#ic-gear"/></svg>Technology and<br>Professional</div>
</section>

<!-- Capital band -->
<div class="capital abs" role="img" aria-label="Hiker standing on a rocky ridge above misty mountain valleys at dusk"></div>
<div class="capital-card abs"><strong>We place capital</strong> for long-term growth and revenue generation. Our investment horizon enables a focus on building strong sustainable companies, with empowered teams maximizing impact.</div>

<!-- Investment experience -->
<div class="wordmark" style="left:40px;top:2256px;width:230px">Ledgerwise</div>
<div class="wordmark" style="left:310px;top:2256px;width:160px">Kestrel AI</div>
<div class="wordmark" style="left:515px;top:2256px;width:160px">Amplify PR</div>
<div class="wordmark" style="left:725px;top:2256px;width:200px">Brightway Avenue</div>
<div class="wordmark" style="left:985px;top:2256px;width:160px">Montessa</div>
<div class="wordmark" style="left:60px;top:2396px;width:220px;font-size:22px">Corvane Capital Partners</div>
<div class="wordmark" style="left:930px;top:2390px;width:190px;font-size:38px">HarborNest</div>
<h2 class="exp-title abs">Investment Experience</h2>
<p class="exp-copy abs">The Altavance Industries team has invested in, managed and served on the boards of a variety of high performing companies.</p>
<div class="wordmark" style="left:25px;top:2533px;width:190px;font-size:36px">tapwallet</div>
<div class="wordmark" style="left:250px;top:2540px;width:170px;font-size:22px">Verano Capital</div>
<div class="wordmark" style="left:450px;top:2536px;width:190px;font-size:28px">Boundless Media</div>
<div class="wordmark" style="left:660px;top:2536px;width:180px;font-size:28px">ShareBridge</div>
<div class="wordmark" style="left:850px;top:2540px;width:140px;font-size:22px">PowerBackers</div>
<div class="wordmark" style="left:1030px;top:2538px;width:130px;font-size:24px">Findwell</div>

<!-- Management team -->
<section class="team abs">
  <h2>Management Team</h2>
  <span class="arrow" style="left:57px"></span>
  <div class="member" style="left:83px"><div class="portrait" role="img" aria-label="Portrait of Garrett Lindqvist"></div><h3>GARRETT</h3><p>Garrett Lindqvist is a Partner at Altavance Industries</p></div>
  <div class="member" style="left:341px"><div class="portrait" role="img" aria-label="Portrait of Tobias Renwick"></div><h3>TOBIAS</h3><p>Tobias Renwick is a Founding Partner at Altavance</p></div>
  <div class="member" style="left:599px"><div class="portrait" role="img" aria-label="Portrait of Nadia Corvell"></div><h3>NADIA</h3><p>Nadia Corvell is a Partner at Altavance Industries</p></div>
  <div class="member" style="left:857px"><div class="portrait" role="img" aria-label="Portrait of Vikram Ashdale"></div><h3>VIKRAM</h3><p>Vikram Ashdale is a Partner Altavance Industries</p></div>
  <span class="arrow" style="left:1096px"></span>
</section>

<!-- Footer -->
<footer class="footer abs" role="img" aria-label="City skyline at dusk behind the footer">
  <div class="brand">Altavance<br>Industries</div>
  <div class="foot-col" style="left:415px"><h4>Quick Links</h4><ul><li>Home</li><li>About Us</li><li>Advisory Services</li><li>Work With Us</li><li>Contact</li></ul></div>
  <div class="foot-col" style="left:646px"><h4>Info Links</h4><ul><li>Our Team</li><li>Enquiry</li><li>Terms Of Services</li><li>Policy</li></ul></div>
  <div class="foot-col" style="left:878px"><h4>Contact Us</h4><ul><li>info@altavanceindustries.example</li><li>-888 8888 8888</li></ul>
    <div class="social"><span></span><span></span><span></span></div></div>
  <div class="foot-rule"></div>
  <div class="copyright">Copyright © 2020 Altavance Industries. All Rights Reserved.</div>
</footer>

</body>
</html>
```